Pine Ridge Traders, LLC- Global Beverage Company with 100% Cold Chain Logistics

Hey All, My Name is Dale, I am a young business owner in a competitive export space, but my niche is that I am shipping all of my beer around the world, "100% Cold Chain". This model is more costly, but it protects the integrity of the beer itself and will give folks in foreign countries the best representation of what US Craft Beer has to offer.

I am not a branding guy and don't claim to be one, I am a salesperson first, and will be referring to all of you to create something great that will be memorable.

I am looking for a basic Business Card Design for my Craft Beer Export company. I sell US Craft Beer in several countries around the globe. Austrailia, China, Taiwan, Chile, France, New Zealand... to name a few.

I am looking for a sleek, modern, and fresh design. Quickly!

Thanks for your consideration!

Cheers,

Dale

Target Market(s)

International

Contact Information for Business Card

Dale Corwin
Founder- Roving Hops Guy
Dale@PineRidgeTraders.example
@RovingHopsGuy- Instagram only
www.Pineridgetraders.example
@PineRidgeTradersAU- Instagram Only

Font styles to use
Serif

Colors
0592cd
ffffff

Requirements
Must have
• Name-
• Title-
• Email-
• Social Media Handle-
• Company Website-
Nice to have
• Nice Logo/ Images on Card
Should not have
• Tacky Beer Images

```html
<!DOCTYPE html>
<html lang="en">
<head>
<meta charset="utf-8">
<title>Pine Ridge Traders, LLC – Business Card</title>
<link rel="stylesheet" href="https://fonts.googleapis.com/css2?family=Tinos:wght@400;700&display=swap">
<style>
  :root {
    --page: #efeae3;
    --card-light: #ecebe8;
    --card-light-edge: #dcdad6;
    --band-blue: #4a8ccc;
    --brand-blue: #4a8ccc;
    --social-blue: #3d6fc4;
    --ink: #111111;
    --white: #ffffff;
    --card-dark: #2a2a2a;
    --card-dark-edge: #1d1d1d;
    --map-tone: rgba(255,255,255,0.05);
    --muted: #d8d8d8;
  }
  * { box-sizing: border-box; margin: 0; padding: 0; }
  html, body { width: 900px; height: 1200px; overflow: hidden; }
  body {
    background: var(--page);
    font-family: "Tinos", "Times New Roman", serif;
    position: relative;
  }
  .card {
    position: absolute;
    left: 88px;
    width: 734px;
    height: 428px;
    border-radius: 22px;
    overflow: hidden;
    box-shadow: 0 6px 14px rgba(0,0,0,0.25);
  }
  .card--front { top: 137px; }
  .card--back { top: 633px; }

  .brand-name {
    position: absolute; left: 0; width: 100%;
    text-align: center; font-weight: 400;
    text-transform: uppercase; line-height: 1;
  }

  /* Divider under the company name: plain rules with an ornament area between */
  .divider-rule {
    position: absolute; height: 2px; width: 50px;
  }
  .divider-ornament {
    position: absolute; width: 240px; height: 22px; border-radius: 50%;
  }

  /* Front */
  .front-panel {
    position: absolute; left: 0; top: 0; width: 100%; height: 288px;
    background: linear-gradient(180deg, var(--card-light), var(--card-light-edge));
  }
  .card--front .brand-name { color: var(--ink); }
  .card--front .brand-name--main { top: 126px; font-size: 52px; letter-spacing: 0.5px; }
  .card--front .brand-name--sub { top: 182px; font-size: 36px; }
  .card--front .divider-rule { top: 243px; background: var(--ink); }
  .card--front .divider-rule--left { left: 187px; }
  .card--front .divider-rule--right { left: 495px; }
  .card--front .divider-ornament {
    left: 245px; top: 232px;
    background: radial-gradient(ellipse at center, rgba(17,17,17,0.55), rgba(17,17,17,0) 72%);
  }

  .contact-band {
    position: absolute; left: 0; top: 288px; width: 100%; height: 140px;
    background: var(--band-blue); color: var(--white);
  }
  .person-name {
    position: absolute; top: 20px; width: 100%; text-align: center;
    font-size: 25px; font-weight: 700;
  }
  .person-title {
    position: absolute; top: 52px; width: 100%; text-align: center;
    font-size: 17px;
  }
  .band-rule {
    position: absolute; left: 36px; right: 46px; top: 76px;
    height: 1px; background: var(--white);
  }
  .contact-item {
    position: absolute; top: 86px; display: flex; align-items: center; gap: 12px;
    font-size: 18px;
  }
  .contact-item--email { left: 36px; }
  .contact-item--web { left: 414px; }
  .contact-icon { width: 32px; height: 32px; flex: none; }

  /* Back */
  .back-panel {
    position: absolute; inset: 0;
    background: linear-gradient(180deg, var(--card-dark), var(--card-dark-edge));
  }
  .map-area {
    position: absolute; left: 30px; top: 40px; width: 680px; height: 330px;
    background: radial-gradient(ellipse at center, var(--map-tone), transparent 70%);
  }
  .card--back .brand-name { color: var(--brand-blue); }
  .card--back .brand-name--main { top: 194px; font-size: 52px; letter-spacing: 0.5px; }
  .card--back .brand-name--sub { top: 250px; font-size: 36px; }
  .card--back .divider-rule { top: 308px; background: var(--brand-blue); }
  .card--back .divider-rule--left { left: 192px; }
  .card--back .divider-rule--right { left: 490px; }
  .card--back .divider-ornament {
    left: 245px; top: 297px;
    background: radial-gradient(ellipse at center, rgba(74,140,204,0.6), rgba(74,140,204,0) 72%);
  }

  .social-row {
    position: absolute; right: 46px; top: 366px;
    display: flex; align-items: center; gap: 8px;
    color: var(--muted); font-size: 17px;
  }
  .social-handle { margin-right: 4px; }
  .social-dot {
    width: 22px; height: 22px; border-radius: 50%; background: var(--social-blue); flex: none;
  }
  .social-network { color: var(--muted); }
</style>
</head>
<body>

<section class="card card--front" aria-label="Business card front">
  <div class="front-panel" role="img" aria-label="Whitewashed wood plank background"></div>
  <p class="brand-name brand-name--main">Pine Ridge</p>
  <p class="brand-name brand-name--sub">Traders, LLC</p>
  <div class="divider-rule divider-rule--left"></div>
  <div class="divider-ornament" role="img" aria-label="Decorative flourish"></div>
  <div class="divider-rule divider-rule--right"></div>

  <div class="contact-band">
    <p class="person-name">Dale Corwin</p>
    <p class="person-title">Founder- Roving Hops Guy</p>
    <div class="band-rule"></div>
    <div class="contact-item contact-item--email">
      <svg class="contact-icon" viewBox="0 0 32 32" aria-hidden="true">
        <circle cx="16" cy="16" r="16" fill="#ffffff"/>
        <rect x="8" y="10.5" width="16" height="11" fill="none" stroke="#4a8ccc" stroke-width="1.8"/>
        <polyline points="8,10.5 16,17 24,10.5" fill="none" stroke="#4a8ccc" stroke-width="1.8"/>
      </svg>
      <span>Dale@PineRidgeTraders.example</span>
    </div>
    <div class="contact-item contact-item--web">
      <svg class="contact-icon" viewBox="0 0 32 32" aria-hidden="true">
        <circle cx="16" cy="16" r="16" fill="#ffffff"/>
        <g fill="none" stroke="#4a8ccc" stroke-width="1.5">
          <circle cx="16" cy="16" r="8.5"/>
          <ellipse cx="16" cy="16" rx="3.8" ry="8.5"/>
          <line x1="7.5" y1="16" x2="24.5" y2="16"/>
          <line x1="9" y1="11.5" x2="23" y2="11.5"/>
          <line x1="9" y1="20.5" x2="23" y2="20.5"/>
        </g>
      </svg>
      <span>www.Pineridgetraders.example</span>
    </div>
  </div>
</section>

<section class="card card--back" aria-label="Business card back">
  <div class="back-panel" role="img" aria-label="Dark wood plank background"></div>
  <div class="map-area" role="img" aria-label="Faint world map behind the company name"></div>
  <p class="brand-name brand-name--main">Pine Ridge</p>
  <p class="brand-name brand-name--sub">Traders, LLC</p>
  <div class="divider-rule divider-rule--left"></div>
  <div class="divider-ornament" role="img" aria-label="Decorative flourish"></div>
  <div class="divider-rule divider-rule--right"></div>
  <div class="social-row">
    <span class="social-handle">@RovingHopsGuy</span>
    <span class="social-dot" aria-hidden="true"></span>
    <span class="social-network">Hopline</span>
  </div>
</section>

</body>
</html>
```